The Horizonfold LLC Asset Classes

I'm looking for for two designs here to go into powerpoint and potentially as a standalone PDF. My company does wealth management.
Graphic Image #1
I break down the investment world into 4 broad categories
-Preservation
-Capital Markets
-Real Estate
-Alternatives
In each broad category, there are subcategories:
Preservation: cash, checking/savings accounts, money market accounts, CD's, and fixed annuities.
Capital Markets: Publicly traded stocks and bonds
Real Estate: single-family residence, retail, industrial, multifamily, and office
Alternatives: private equity, private credit, cryptocurrency, asset-backed loans, tax liens, oil & gas, litigation finance, and royalties
Graphic 2: Please see the bottom f page 1 of the Lanternway Briefings PDF.
Just like in graphic one, you have 4 categories of the Capital Markets and their respective subcategories
Category 1: Domestic Stocks: Subcategories are Large, mid, and small size companies
Category 2: International Stocks: Subcategories are Large, Mid/Small and by region - Developed and Emerging
Category 3: Fixed Income: You have subcategories like corporate, municipal, government, domestic, international
Category 4: Alternatives: The subcategories are metals and real estate
---------------------
I'm looking to create a graphic (either pie chart, or a circle broken into parts or some other clever way to illustrate this) to clearly illustrate both of these universes in a clean, professional, slick manner.
Target Market(s)
Investors
Colors
Designer to choose colors to be used in the design.
Requirements
Must have
- Clean
- professional
- Easy to read
- Creative
- Visually appealling
Nice to have
- I have attached my logo and some marketing materials so you can get a feel of what I am doing. Maybe you can clean this up too!

```html
<!DOCTYPE html>
<html lang="en">
<head>
<meta charset="utf-8">
<title>Capital Markets — The Horizonfold LLC</title>
<link rel="stylesheet" href="https://fonts.googleapis.com/css2?family=Fira+Sans:wght@300;400;500&family=Nunito:wght@800;900&display=swap">
<style>
  :root {
    --page-bg: #eceded;
    --slide-bg: #ffffff;
    --title-orange: #f28a3f;
    --domestic-green: #45ae45;
    --international-blue: #0869ad;
    --fixed-orange: #f99734;
    --alt-gray: #a3a3a3;
    --body-text: #4a4a4a;
    --brand-teal: #17587f;
    --ring-orange: #efaa5c;
  }
  * { box-sizing: border-box; margin: 0; padding: 0; }
  html, body { width: 1200px; height: 1000px; overflow: hidden; background: var(--page-bg); }
  .slide {
    position: absolute; left: 0; top: 50px;
    width: 1200px; height: 900px;
    background: var(--slide-bg);
    font-family: "Fira Sans", sans-serif;
  }
  .slide-title {
    position: absolute; left: 48px; top: 44px;
    font-weight: 400; font-size: 45px; line-height: 1;
    color: var(--title-orange); letter-spacing: 0.5px;
  }
  .brand-mark {
    position: absolute; left: 880px; top: 58px;
    display: flex; align-items: center; gap: 12px;
  }
  .brand-dot { width: 34px; height: 34px; border-radius: 50%; background: var(--brand-teal); }
  .brand-name { font-size: 27px; font-weight: 500; color: var(--brand-teal); white-space: nowrap; }
  .market-wheel { position: absolute; left: 0; top: 0; }
  .segment-label {
    font-family: "Nunito", sans-serif; font-weight: 900; font-size: 23px;
    fill: #ffffff; text-anchor: middle; letter-spacing: 0.3px;
  }
  .center-name { font-family: "Fira Sans", sans-serif; font-weight: 500; font-size: 16px; fill: var(--brand-teal); text-anchor: middle; }
  .callout {
    position: absolute; font-size: 18px; line-height: 23px; color: var(--body-text);
  }
  .callout ul { list-style: none; }
  .callout li { position: relative; padding-left: 15px; }
  .callout li::before { content: "•"; position: absolute; left: 0; }
  .callout-domestic { left: 168px; top: 265px; }
  .callout-international { left: 912px; top: 258px; }
  .callout-alternatives { left: 168px; top: 698px; }
  .callout-fixed { left: 896px; top: 698px; }
</style>
</head>
<body>
<main class="slide">
  <h1 class="slide-title">Capital Markets</h1>

  <div class="brand-mark">
    <span class="brand-dot"></span>
    <span class="brand-name">The Horizonfold LLC</span>
  </div>

  <svg class="market-wheel" width="1200" height="900" viewBox="0 0 1200 900">
    <defs>
      <filter id="soft-shadow" x="-20%" y="-20%" width="140%" height="140%">
        <feDropShadow dx="-6" dy="10" stdDeviation="12" flood-color="#000" flood-opacity="0.22"/>
      </filter>
      <radialGradient id="hub-fill" cx="40%" cy="30%" r="75%">
        <stop offset="0" stop-color="#ffffff"/>
        <stop offset="1" stop-color="#d9d9da"/>
      </radialGradient>
    </defs>

    <!-- callout connectors -->
    <g class="connectors" stroke-width="1.2" fill="none">
      <polyline points="207,250 398,250" stroke="var(--domestic-green)"/>
      <polyline points="749,216 979,216 979,246" stroke="var(--international-blue)"/>
      <polyline points="364,643 213,643 213,673" stroke="var(--alt-gray)"/>
      <polyline points="824,677 948,677" stroke="var(--fixed-orange)"/>
    </g>
    <g class="connector-dots">
      <circle cx="207" cy="250" r="3.5" fill="var(--domestic-green)"/>
      <circle cx="979" cy="246" r="3.5" fill="var(--international-blue)"/>
      <circle cx="213" cy="673" r="3.5" fill="var(--alt-gray)"/>
      <circle cx="948" cy="677" r="3.5" fill="var(--fixed-orange)"/>
    </g>

    <!-- segments -->
    <g class="segments" filter="url(#soft-shadow)">
      <path class="segment-alternatives" d="M616 489 L616 784 A295 295 0 0 1 321 489 Z" fill="var(--alt-gray)"/>
      <path class="segment-fixed-income" d="M616 489 L896 489 A280 280 0 0 1 616 769 Z" fill="var(--fixed-orange)"/>
      <path class="segment-international" d="M616 489 L616 187 A302 302 0 0 1 918 489 Z" fill="var(--international-blue)"/>
      <path class="segment-domestic" d="M616 489 L290 489 A326 326 0 0 1 616 163 Z" fill="var(--domestic-green)"/>
    </g>

    <text class="segment-label" x="453" y="332">Domestic</text>
    <text class="segment-label" x="453" y="359">Stocks</text>
    <text class="segment-label" x="746" y="332">International</text>
    <text class="segment-label" x="746" y="359">Stocks</text>
    <text class="segment-label" x="743" y="621">Fixed</text>
    <text class="segment-label" x="743" y="648">Income</text>
    <text class="segment-label" x="484" y="637">Alternatives</text>

    <!-- hub -->
    <g class="hub">
      <circle cx="616" cy="489" r="120" fill="url(#hub-fill)" filter="url(#soft-shadow)"/>
      <circle cx="616" cy="489" r="105" fill="none" stroke="var(--ring-orange)" stroke-width="2.5"/>
      <text class="center-name" x="616" y="495">The Horizonfold LLC</text>
    </g>
  </svg>

  <div class="callout callout-domestic">Large, mid,<br>and small<br>companies</div>
  <div class="callout callout-international">
    <ul><li>Large, mid/small</li><li>Developed and<br>Emerging</li></ul>
  </div>
  <div class="callout callout-alternatives">
    <ul><li>Metals</li><li>Real Estate</li></ul>
  </div>
  <div class="callout callout-fixed">
    <ul><li>Corporate</li><li>Municipal</li><li>Government</li><li>Domestic</li><li>International</li></ul>
  </div>
</main>
</body>
</html>
```